Logo+Business Card Design for Architecture Photographer

Hi Everyone,

I am looking for logo/business designs for my new business - Brovald Studio. My business does commercial photography with a specialization in architecture, luxury real estate, and design. The Int is short for interior and ex is short for exterior.

Some of the values of my business are:
- providing top quality photography and post-processing (straight lines, accurate and bold whites/blacks/colors) for commercial use (websites, social media, advertising campaigns)
- fostering a collaborative workflow that is professional and fun that will have clients returning because of the premium service they received
- asking the right questions so that I can capture what matters to my clients with my own creative vision

I want my final look to be modern and bold. The business cards will be letter pressed/debossed, so the design should incorporate that. I am imagining a solid matte olive green or matte navy blue background on one side and white on the other. The card will be printed on colored cards, so you don't have to put a colored background as part of the design. I have attached some examples of colors I like, although it doesn't matter too much for the purpose of your work.

I want the debossing to be part of the design of the business card. This debossing should be some some of pattern or a frame that holds the logo on the back of the card (I have attached some sample images named geometric debossing to show what I mean). Then I can just foil print my logo on the back. My contact info and a logo will be on the front.

Somewhere it should say "Architecture, Luxury Real Estate, Design".

My vision for the logo: no cameras or buildings. I can't think of anything symbolic for the logo, but it should somehow contain Brovald. It might be cool to have them separated by a line like Bro | Vald. Or have the Int inside something, and the Ex outside.

I plan on using Quelmark to print the cards. You can find their specifications here: https://quelmark.example/products/duplex-business-cards?variant=4837201956372

It would be nice to have a psd file that I can edit as well as a PDF to deliver to the printing company. Both must be vector graphics.

Thank you to everyone who has submitted a design as it has helped me get a better idea of what I want.

Target Market(s)

Designers, architects

Industry/Entity Type

Photographer

Contact Information for Business Card

See project description

Logo Text

Brovald Studio

Font styles to use
Sans Serif
Decorative

Colors
ffffff

Requirements
Must have
• Logo and business card design. Deboss area less than 3 square inches. Deboss area should be some sort of a pattern/design as shown in attachments labelled "Geometric Debossing Example".
• Logo design and deboss design must be submitted in vector graphics.
Nice to have
• Color doesn't have to be shown on the design because I will be printing on colored paper, although it would be helpful to help me visualize what it will eventually look like.
Should not have
• A camera or building in the design...too cliche.

```html
<!DOCTYPE html>
<html lang="en">
<head>
<meta charset="utf-8">
<title>Brovald Studio – Business Card</title>
<link rel="stylesheet" href="https://fonts.googleapis.com/css2?family=Fira+Sans:wght@300;400;500&display=swap">
<style>
  :root {
    --brand-blue: #0f56a6;
    --card-white: #ffffff;
    --backdrop: #2b2b2b;
    --text-on-blue: #ffffff;
  }
  * { margin: 0; padding: 0; box-sizing: border-box; }
  html, body {
    width: 1200px;
    height: 900px;
    overflow: hidden;
    background: var(--backdrop);
    font-family: "Fira Sans", sans-serif;
  }
  .canvas {
    position: relative;
    width: 1200px;
    height: 900px;
  }
  .card {
    position: absolute;
    left: 270px;
    width: 660px;
    height: 378px;
    overflow: hidden;
  }
  .card-back {
    top: 36px;
    background: var(--brand-blue);
  }
  .card-front {
    top: 480px;
    background: var(--card-white);
  }
  .wordmark {
    position: absolute;
    font-weight: 300;
    white-space: nowrap;
    text-align: center;
    letter-spacing: 1px;
  }
  .card-back .wordmark {
    left: 0;
    right: 0;
    top: 150px;
    font-size: 46px;
    color: var(--text-on-blue);
  }
  .card-front .wordmark {
    left: 20px;
    width: 280px;
    top: 142px;
    font-size: 34px;
    color: var(--brand-blue);
  }
  .divider {
    position: absolute;
    left: 318px;
    top: 78px;
    width: 2px;
    height: 150px;
    background: var(--brand-blue);
  }
  .contact {
    position: absolute;
    left: 342px;
    top: 76px;
    color: var(--brand-blue);
  }
  .contact-name {
    font-size: 21px;
    font-weight: 500;
    letter-spacing: 0.3px;
  }
  .contact-title {
    font-size: 15px;
    font-weight: 500;
    margin-top: 2px;
    margin-left: 5px;
  }
  .contact-list {
    list-style: none;
    margin-top: 16px;
    margin-left: 12px;
  }
  .contact-list li {
    display: flex;
    align-items: center;
    gap: 12px;
    font-size: 16px;
    font-weight: 400;
    line-height: 24px;
  }
  .contact-list svg {
    width: 14px;
    height: 14px;
    fill: var(--brand-blue);
    flex: none;
  }
  .address-band {
    position: absolute;
    left: 0;
    bottom: 0;
    width: 100%;
    height: 56px;
    background: var(--brand-blue);
    color: var(--text-on-blue);
    font-size: 16px;
    font-weight: 500;
    display: flex;
    align-items: flex-start;
    justify-content: center;
    padding-top: 8px;
  }
</style>
</head>
<body>
<main class="canvas">
  <section class="card card-back" aria-label="Card back">
    <div class="wordmark">Brovald Studio</div>
  </section>

  <section class="card card-front" aria-label="Card front">
    <div class="wordmark">Brovald Studio</div>
    <div class="divider"></div>
    <div class="contact">
      <div class="contact-name">YOUR NAME</div>
      <div class="contact-title">Your Title</div>
      <ul class="contact-list">
        <li>
          <svg viewBox="0 0 24 24" aria-hidden="true"><path d="M6.6 10.8a15.1 15.1 0 0 0 6.6 6.6l2.2-2.2c.3-.3.7-.4 1-.2 1.1.4 2.3.6 3.6.6.6 0 1 .4 1 1V20c0 .6-.4 1-1 1A17 17 0 0 1 3 4c0-.6.4-1 1-1h3.5c.6 0 1 .4 1 1 0 1.3.2 2.5.6 3.6.1.3 0 .7-.2 1z"/></svg>
          123-456-2100
        </li>
        <li>
          <svg viewBox="0 0 24 24" aria-hidden="true"><path d="M2 5h20v14H2z M3.5 6.5 12 13l8.5-6.5" fill="none" stroke="#0f56a6" stroke-width="2"/><path d="M2 5h20L12 12.5z"/></svg>
          youremail@mailbox.example
        </li>
        <li>
          <svg viewBox="0 0 24 24" aria-hidden="true"><circle cx="12" cy="12" r="10"/><path d="M2 12h20M12 2c3 3 3 17 0 20M12 2c-3 3-3 17 0 20" fill="none" stroke="#ffffff" stroke-width="1.5"/></svg>
          www.yourwebsite.com
        </li>
      </ul>
    </div>
    <div class="address-band">Your address, city, state, ZIP 0000</div>
  </section>
</main>
</body>
</html>
```